QLDR Individual and Corporate Development Business Card Design

QLDR needs a business card design that is aligned with it's values and targetted markets. Harmonic Ladder of Reasoning Matrix's self diagnosis model and tools, which can be used for personal improvement and team/business performance enhancement, is based on the learnings of over 20 years of medical practitioning. QLDR supercharges personal effectiveness and awareness to also increase team and business performance.

The targetted markets are high performance individuals and teams who aspire seek to enhance their capabilities and achieve their absolute best potential.

Look and feel for the business card design we are looking for is high technology, premium, fresh, new and medical.

Target Market(s)

Industry/Entity Type

Business Consultant

Contact Information for Business Card

Logo, Full Name, Title, Phone number, Email, company name, Address,

Font styles to use
Sans Serif

Requirements
Must have
• Tag line: Maximising Performance for Highly Effective People
• Please use same colours as the logo.

```html
<!DOCTYPE html>
<html lang="en">
<head>
<meta charset="utf-8">
<title>QLDR Business Card</title>
<link href="https://fonts.googleapis.com/css2?family=Questrial&family=Open+Sans:wght@400&display=swap" rel="stylesheet">
<style>
  :root {
    --teal: #1fb3cc;
    --grey: #8a8f94;
    --black: #0b0b0c;
    --white: #ffffff;
    --stage: #2a2b2d;
    --line: #55585c;
  }
  * { margin: 0; padding: 0; box-sizing: border-box; }
  html, body { width: 1200px; height: 900px; overflow: hidden; background: var(--stage); }
  .canvas { position: relative; width: 1200px; height: 900px; }
  .card {
    position: absolute; left: 260px; width: 680px; height: 389px;
    overflow: hidden; box-shadow: 0 10px 30px rgba(0,0,0,.5);
  }
  .card--front { top: 42px; background: var(--black); }
  .card--back { top: 469px; background: var(--white); }

  .brand { position: absolute; text-align: left; }
  .brand__mark {
    font-family: "Questrial", sans-serif; color: var(--teal);
    letter-spacing: 6px; line-height: 1; display: flex; align-items: center; gap: 14px;
  }
  .brand__dot { border-radius: 50%; background: var(--teal); display: inline-block; }
  .brand__rule { height: 2px; background: var(--line); }
  .brand__name {
    font-family: "Questrial", sans-serif; text-transform: uppercase; letter-spacing: 2px;
    line-height: 1.15;
  }
  .brand__name .lead { color: var(--teal); }
  .brand__name .tail { color: var(--grey); }
  .tagline {
    font-family: "Open Sans", sans-serif; color: var(--grey);
    font-style: normal; letter-spacing: .5px;
  }

  .card--front .brand { left: 140px; top: 100px; width: 420px; }
  .card--front .brand__mark { font-size: 96px; }
  .card--front .brand__dot { width: 22px; height: 22px; }
  .card--front .brand__rule { margin: 14px 0 10px; }
  .card--front .brand__name { font-size: 21px; }
  .card--front .tagline { font-size: 14px; margin-top: 16px; }

  .card--back .brand { left: 230px; top: 46px; width: 300px; }
  .card--back .brand__mark { font-size: 62px; }
  .card--back .brand__dot { width: 14px; height: 14px; }
  .card--back .brand__rule { margin: 9px 0 7px; background: #c9cdd0; }
  .card--back .brand__name { font-size: 14px; }
  .card--back .tagline { font-size: 11px; margin-top: 10px; white-space: nowrap; }

  .band {
    position: absolute; left: 0; bottom: 0; width: 100%; height: 150px;
    background: var(--black);
  }
  .person { position: absolute; left: 50px; bottom: 38px; font-family: "Questrial", sans-serif; }
  .person__name { color: var(--white); font-size: 44px; line-height: 1; }
  .person__title { color: var(--teal); font-size: 26px; line-height: 1.1; }

  .contact {
    position: absolute; right: 40px; top: 28px; list-style: none;
    font-family: "Open Sans", sans-serif; color: var(--white); font-size: 15px;
    text-align: right; line-height: 1.5;
  }
  .contact li { display: flex; justify-content: flex-end; align-items: center; gap: 8px; }
  .contact svg { width: 14px; height: 14px; fill: var(--teal); flex: none; }
  .contact .indent { padding-right: 22px; }
</style>
</head>
<body>
<div class="canvas">

  <section class="card card--front">
    <div class="brand">
      <div class="brand__mark"><span>QLDR</span><span class="brand__dot"></span></div>
      <div class="brand__rule"></div>
      <div class="brand__name"><span class="lead">Harmonic Ladder</span><br><span class="tail">of</span> <span class="lead">Reasoning Matrix</span></div>
      <p class="tagline">Maximising Performance for Highly Effective People</p>
    </div>
  </section>

  <section class="card card--back">
    <div class="brand">
      <div class="brand__mark"><span>QLDR</span><span class="brand__dot"></span></div>
      <div class="brand__rule"></div>
      <div class="brand__name"><span class="lead">Harmonic Ladder</span><br><span class="tail">of</span> <span class="lead">Reasoning Matrix</span></div>
      <p class="tagline">Maximising Performance for Highly Effective People</p>
    </div>

    <div class="band">
      <div class="person">
        <div class="person__name">Your Name</div>
        <div class="person__title">Manager</div>
      </div>
      <ul class="contact">
        <li>(01) 0000 8888
          <svg viewBox="0 0 24 24"><path d="M6.6 10.8a15 15 0 0 0 6.6 6.6l2.2-2.2c.3-.3.7-.4 1-.2 1.1.4 2.3.6 3.6.6.6 0 1 .4 1 1V20c0 .6-.4 1-1 1A17 17 0 0 1 3 4c0-.6.4-1 1-1h3.5c.6 0 1 .4 1 1 0 1.3.2 2.5.6 3.6.1.3 0 .7-.2 1z"/></svg></li>
        <li>info@yourdomain.com
          <svg viewBox="0 0 24 24"><path d="M2 5h20v14H2z M3 6l9 7 9-7" fill="none" stroke="#1fb3cc" stroke-width="2"/></svg></li>
        <li>Suites 14/15, Level 3
          <svg viewBox="0 0 24 24"><path d="M12 2a7 7 0 0 0-7 7c0 5 7 13 7 13s7-8 7-13a7 7 0 0 0-7-7zm0 9.5A2.5 2.5 0 1 1 12 6.5a2.5 2.5 0 0 1 0 5z"/></svg></li>
        <li class="indent">48 Harbour Rd. Eastvale</li>
      </ul>
    </div>
  </section>

</div>
</body>
</html>
```